Flyer for an online formula one racing league

Hello.

I am looking for the perfect one page facebook/instagram style flyer for an online formula one racing league. The racing league is called 'VOLTA RACING LEAGUE'.

Information that MUST be on the new flyer is already on the old flyer I have uploaded here. In addition to including: The Volta racing league 'V' logo I have uploaded AND the text: 'Very popular, clean and competitive racing league, running for its 4th season. Why not join with a friend? Race times, Mondays, Tuesdays and Wednesdays each at 8pm UK TIME Message below for any questions. (Spacing of information is not important, however all the information in regards to the racing I have just mentioned MUST BE on the flyer, this includes info from old pic, logo and the other info I just mentioned).

It would be beneficial to have lots of dark blue on the flyer and the new flyer to be a lot different to the original flyer I uploaded, but this is not essential.

I apologise if I did not explain very well, any questions, please message me.

The best flyer should look the most attractive to someone that might be interested in joining an online formula one racing league.

I used this website before to create the perfect logo for my Sunday League team last year, and I was very impressed. I look forward to seeing your submissions.

Target Market(s)

No specific target, more something that may attract someone into joining a formula one online racing league

Industry/Entity Type

e sports/formula one

Colors
0054AA
0677BA
7BADD7
CADEEF
E8F1F8

Requirements
Must have
• Read product description please
Should not have
• Ignoring product description!

```html
<!DOCTYPE html>
<html lang="en">
<head>
<meta charset="utf-8">
<title>Volta Racing League Flyer</title>
<link href="https://fonts.googleapis.com/css2?family=Bebas+Neue&family=Poppins:wght@400;700;800&display=swap" rel="stylesheet">
<style>
  :root {
    --stage: #d6d6d6;
    --paper: #ffffff;
    --navy: #101d6e;
    --ink-dark: #0a1240;
    --pink: #e6007e;
    --yellow: #ffd400;
    --royal: #13308f;
    --royal-deep: #0c2379;
    --white: #ffffff;
  }
  * { margin: 0; padding: 0; box-sizing: border-box; }
  html, body {
    width: 1200px; height: 900px; overflow: hidden;
    background: var(--stage);
  }
  .flyer {
    position: absolute; left: 0; top: 136px;
    width: 1200px; height: 628px;
    background: var(--paper);
    overflow: hidden;
    font-family: "Poppins", sans-serif;
  }
  .flag-decor {
    position: absolute; right: 0; top: 0;
    width: 520px; height: 253px;
    background: linear-gradient(200deg, #e4e4e4 0%, #f2f2f2 45%, rgba(255,255,255,0) 80%);
  }
  .brand-mark {
    position: absolute; left: 58px; top: 55px;
    width: 176px; height: 176px; border-radius: 50%;
    background: var(--ink-dark);
    display: flex; align-items: center; justify-content: center;
    font-family: "Bebas Neue", sans-serif;
    font-size: 46px; color: var(--white); letter-spacing: 1px;
  }
  .league-title {
    position: absolute; left: 268px; top: 58px; width: 880px;
    font-family: "Bebas Neue", sans-serif;
    font-size: 126px; line-height: 1; letter-spacing: 0;
    color: var(--pink); white-space: nowrap;
  }
  .league-title .lead { color: var(--navy); }
  .league-tagline {
    position: absolute; left: 268px; top: 178px; width: 880px;
    font-family: "Bebas Neue", sans-serif;
    font-size: 53px; line-height: 1; letter-spacing: -0.6px;
    color: var(--navy); white-space: nowrap;
    text-align: justify; text-align-last: justify;
  }
  .season-band {
    position: absolute; left: 0; top: 253px; width: 1200px; height: 72px;
    background: var(--yellow);
    display: flex; align-items: center; justify-content: center;
    font-weight: 800; font-size: 72px; line-height: 1;
    color: var(--navy); white-space: nowrap; padding-top: 4px;
  }
  .info-panel {
    position: absolute; left: 0; top: 325px; width: 1200px; height: 303px;
    background: radial-gradient(ellipse at 40% 40%, var(--royal) 0%, var(--royal-deep) 100%);
    color: var(--white);
  }
  .invite {
    position: absolute; left: 0; top: 12px; width: 1200px;
    text-align: center; font-weight: 800; font-size: 56px; line-height: 1.1;
  }
  .divisions {
    position: absolute; left: 0; top: 76px; width: 1200px;
    text-align: center; font-weight: 700; font-size: 31px; line-height: 1.2;
  }
  .dotted-rule {
    position: absolute; left: 58px; top: 137px; width: 1092px;
    border-top: 3px dotted rgba(255,255,255,0.85);
  }
  .race-times-tag {
    position: absolute; left: 55px; top: 160px; width: 181px; height: 50px;
    background: var(--pink);
    font-family: "Bebas Neue", sans-serif; font-size: 46px; line-height: 54px;
    text-align: center; color: var(--white);
  }
  .schedule {
    position: absolute; left: 250px; top: 160px;
    font-weight: 700; font-size: 27px; line-height: 34px; white-space: nowrap;
  }
  .highlight { color: var(--yellow); }
  .contact-note {
    position: absolute; left: 55px; top: 226px;
    font-weight: 400; font-size: 21px; letter-spacing: 0.3px; white-space: nowrap;
  }
  .column-divider {
    position: absolute; left: 796px; top: 151px; height: 98px;
    border-left: 2px dashed rgba(255,255,255,0.8);
  }
  .availability {
    position: absolute; left: 820px; top: 156px;
    font-size: 27px; line-height: 29px; white-space: nowrap;
  }
  .availability .days { font-weight: 700; color: var(--yellow); display: block; }
</style>
</head>
<body>
  <main class="flyer">
    <div class="flag-decor" role="img" aria-label="Faint chequered racing flag decoration"></div>

    <div class="brand-mark">VOLTA</div>

    <h1 class="league-title"><span class="lead">VOLTA</span> RACING LEAGUE</h1>
    <p class="league-tagline">Very popular, clean and competitive racing league</p>

    <div class="season-band">RUNNING FOR ITS 4TH SEASON</div>

    <section class="info-panel">
      <h2 class="invite">WHY NOT JOIN WITH A FRIEND?</h2>
      <p class="divisions">3 DIVISIONS CURRENTLY AND LOOKING TO KEEP GROWING!</p>

      <div class="dotted-rule"></div>

      <div class="race-times-tag">RACE TIMES</div>
      <p class="schedule">
        <span class="highlight">Mondays, Tuesdays</span> and<br>
        <span class="highlight">Wednesdays</span> each at <span class="highlight">8PM</span> UK TIME
      </p>
      <p class="contact-note">MASSAGE BELOW FOR ANY QUESTIONS</p>

      <div class="column-divider"></div>

      <p class="availability">
        SPACES LEFT ON
        <span class="days">MONDAYS,TUESDAY &amp;</span>
        <span class="days">WEDNESDAYS!!!</span>
      </p>
    </section>
  </main>
</body>
</html>
```